Flyer-Design für Business Center
Zielgruppe
Wir sind Co-Working /Business Center Anbieter auf Basis eines Mitgliedschaft Konzeptes. Bei uns kann man Arbeitsplätze und Büroräume mit Kaffee und Wasser in einer Lounge anmieten. Dazu bieten wir Bedarfsgerechte Mitgliedschaften an. Unsere Kunden sind Kreative, Programmierer, Freiberufler aber auch größere Unternehmen.
Aufgabenstellung
DIN LANG A 4, der Flyer wird gedruckt und kommt in Aussteller. Er soll als Eye Catcher den Preis ab 69,90 für 4 Wochen beinhalten. In diesem Preis ist alles inclusive. Also Wasser, Kaffee, Cappuccino, Drucker, Kopierer, Möbel, Putzfrau, Schreibtisch. Bürostuhl. Gleichzeitig soll der Flyer auch als PDF versendet werden können.
Weitere Information findet man auf unserer Webseite www.kranichfeldwerk.com

```html
<!DOCTYPE html>
<html lang="de">
<head>
<meta charset="utf-8">
<title>Kranichfeld Werk – Co-Working &amp; Business Center</title>
<link rel="stylesheet" href="https://fonts.googleapis.com/css2?family=Open+Sans:wght@400;600&display=swap">
<style>
  :root {
    --blue: #29a8e0;
    --blue-dark: #2496d0;
    --text-muted: #56748a;
    --white: #ffffff;
    --page-bg: #eaf2f7;
    --photo-warm: #c9b39c;
    --photo-light: #e8ddd0;
  }
  * { margin: 0; padding: 0; box-sizing: border-box; }
  html, body { width: 1040px; height: 1200px; overflow: hidden; }
  body {
    background: var(--page-bg);
    font-family: "Open Sans", sans-serif;
    position: relative;
  }
  .flyer {
    position: absolute;
    left: 240px; top: 40px;
    width: 560px; height: 1120px;
    background: var(--white);
    box-shadow: 0 10px 30px rgba(0,0,0,.18);
    overflow: hidden;
  }
  .header { position: absolute; left: 0; top: 0; width: 100%; height: 161px; }
  .brand {
    position: absolute; left: 48px; top: 60px;
    display: flex; align-items: center; gap: 10px;
    color: var(--blue-dark); font-weight: 400; font-size: 27px; line-height: 1.1;
  }
  .brand-dot { width: 16px; height: 16px; border-radius: 50%; background: var(--blue-dark); flex: none; }
  .headline {
    position: absolute; left: 281px; top: 74px;
    color: var(--blue-dark); font-weight: 400; font-size: 27px; line-height: 1.22;
  }
  .tagline-band {
    position: absolute; left: 0; top: 161px; width: 100%; height: 153px;
    background: var(--blue);
    display: flex; align-items: center; justify-content: center;
    padding-bottom: 12px;
  }
  .tagline { color: var(--white); font-size: 19.5px; font-weight: 600; }
  .photo {
    position: absolute; left: 0; top: 314px; width: 100%; height: 372px;
    background: linear-gradient(160deg, var(--photo-light) 0%, var(--photo-warm) 55%, #8f7a68 100%);
  }
  .photo-strip { position: absolute; left: 0; top: 686px; width: 100%; height: 29px; background: var(--blue); }
  .price-badge { position: absolute; left: 319px; top: 552px; width: 224px; height: 224px; }
  .price-text {
    position: absolute; left: 319px; top: 552px; width: 224px; height: 224px;
    color: var(--white);
  }
  .price-ab { position: absolute; left: 44px; top: 108px; font-size: 20px; font-weight: 400; }
  .price-amount { position: absolute; left: 68px; top: 58px; font-size: 58px; font-weight: 600; letter-spacing: -1px; }
  .price-period { position: absolute; left: 130px; top: 128px; font-size: 20px; font-weight: 400; }
  .benefits { position: absolute; left: 50px; top: 738px; }
  .benefits-title { color: var(--blue-dark); font-size: 21.5px; font-weight: 600; margin-bottom: 12px; }
  .benefit-list { list-style: none; }
  .benefit-item {
    display: flex; align-items: center; gap: 12px;
    color: var(--text-muted); font-size: 20px; height: 41.5px;
  }
  .benefit-item svg { flex: none; }
  .footer {
    position: absolute; left: 0; top: 967px; width: 100%; height: 153px;
    background: var(--blue);
    display: flex; flex-direction: column; align-items: center; justify-content: center;
    gap: 9px;
  }
  .contact { display: flex; align-items: center; gap: 10px; color: var(--white); font-size: 20px; line-height: 28px; }
</style>
</head>
<body>
  <main class="flyer">
    <header class="header">
      <div class="brand"><span class="brand-dot"></span><span>Kranichfeld<br>Werk</span></div>
      <h1 class="headline">Co-Working &amp;<br>Business Center</h1>
    </header>

    <section class="tagline-band">
      <p class="tagline">Jetzt Mitglied werden und dauerhaft profitieren</p>
    </section>

    <div class="photo" role="img" aria-label="Foto: Team arbeitet gemeinsam an einem Tisch in einem hellen Co-Working-Loft, Blick von oben"></div>
    <div class="photo-strip"></div>

    <svg class="price-badge" viewBox="0 0 224 224" aria-hidden="true">
      <circle cx="112" cy="112" r="111" fill="none" stroke="#29a8e0" stroke-width="2"/>
      <circle cx="112" cy="112" r="109" fill="#ffffff"/>
      <circle cx="112" cy="112" r="103" fill="#29a8e0"/>
    </svg>
    <div class="price-text">
      <span class="price-ab">ab</span>
      <span class="price-amount">69€</span>
      <span class="price-period">p.M.</span>
    </div>

    <section class="benefits">
      <h2 class="benefits-title">Deine Vorteile:</h2>
      <ul class="benefit-list">
        <li class="benefit-item"><svg width="18" height="18" viewBox="0 0 18 18"><circle cx="9" cy="9" r="9" fill="#56748a"/><path d="M5 9.3l2.6 2.5L13 6.5" fill="none" stroke="#fff" stroke-width="2"/></svg>Events und Netzwerke</li>
        <li class="benefit-item"><svg width="18" height="18" viewBox="0 0 18 18"><circle cx="9" cy="9" r="9" fill="#56748a"/><path d="M5 9.3l2.6 2.5L13 6.5" fill="none" stroke="#fff" stroke-width="2"/></svg>Hochwertige Büroausstattung</li>
        <li class="benefit-item"><svg width="18" height="18" viewBox="0 0 18 18"><circle cx="9" cy="9" r="9" fill="#56748a"/><path d="M5 9.3l2.6 2.5L13 6.5" fill="none" stroke="#fff" stroke-width="2"/></svg>Moderne Technik &amp; Schickes Design</li>
        <li class="benefit-item"><svg width="18" height="18" viewBox="0 0 18 18"><circle cx="9" cy="9" r="9" fill="#56748a"/><path d="M5 9.3l2.6 2.5L13 6.5" fill="none" stroke="#fff" stroke-width="2"/></svg>Gratis Ordnung &amp; Sauberkeit</li>
      </ul>
    </section>

    <footer class="footer">
      <div class="contact">
        <svg width="18" height="18" viewBox="0 0 24 24"><path fill="#fff" d="M6.6 10.8a15.1 15.1 0 006.6 6.6l2.2-2.2c.3-.3.7-.4 1-.2 1.1.4 2.3.6 3.6.6.6 0 1 .4 1 1V20c0 .6-.4 1-1 1A17 17 0 013 4c0-.6.4-1 1-1h3.5c.6 0 1 .4 1 1 0 1.3.2 2.5.6 3.6.1.3 0 .7-.2 1z"/></svg>
        <span>+49-000-418236-00</span>
      </div>
      <div class="contact">
        <svg width="22" height="16" viewBox="0 0 22 16"><rect x="1" y="1" width="20" height="14" rx="1.5" fill="none" stroke="#fff" stroke-width="1.6"/><path d="M1.5 2l9.5 7 9.5-7" fill="none" stroke="#fff" stroke-width="1.6"/></svg>
        <span>info@kranichfeldwerk.com</span>
      </div>
      <div class="contact">
        <svg width="20" height="20" viewBox="0 0 20 20"><circle cx="10" cy="10" r="9" fill="#fff"/><path d="M6 5c2 1 1 3 3 3s1 3 3 3-1 3 0 5M13 3.5c-1 2 1 2 2 3" fill="none" stroke="#29a8e0" stroke-width="1.6"/></svg>
        <span>www.kranichfeldwerk.com</span>
      </div>
    </footer>
  </main>
</body>
</html>
```